Quellin Rebranded Website boutique fitness studio

Looking for a simple, easy to navigate, aesthetically pleasing update of our rebranded website

Target Market(s)

Stay at home moms, discretionary income, fitness and wellness

Coding

Coded - Design and coding required

Number of Pages Required

1 page

Font styles to use
Sans Serif

Colors
0054AA
0677BA
7BADD7
CADEEF
E8F1F8

Requirements
Must have
• Instagram feed linked, "as seen in" banner, spot for studio video at a later date

```html
<!DOCTYPE html>
<html lang="en">
<head>
<meta charset="utf-8">
<title>Quellin — Elevated Strength</title>
<link href="https://fonts.googleapis.com/css2?family=Archivo:wght@800;900&family=Inter:wght@400;500;600;700&display=swap" rel="stylesheet">
<style>
:root{
  --blue:#0054AA;
  --blue-deep:#003E80;
  --blue-mid:#0677BA;
  --sky:#7BADD7;
  --mist:#CADEEF;
  --ice:#E8F1F8;
  --ink:#0b2547;
  --muted:#4d6580;
  --white:#fff;
}
*{box-sizing:border-box;margin:0;padding:0}
html,body{width:1200px;height:5357px;overflow:hidden}
body{font-family:"Inter",sans-serif;color:var(--ink);background:var(--ice);position:relative}
.display{font-family:"Archivo",sans-serif;font-weight:900;text-transform:uppercase;letter-spacing:.5px}
.abs{position:absolute}
.btn{position:absolute;display:flex;align-items:center;justify-content:center;border-radius:22px;font-size:10px;font-weight:700;letter-spacing:.6px;text-transform:uppercase}
.btn-primary{background:var(--blue);color:#fff}
.btn-mid{background:var(--blue-mid);color:#fff}
.btn-soft{background:var(--mist);color:var(--ink)}
.btn-light{background:var(--ice);color:var(--blue)}
.eyebrow{font-size:17px;letter-spacing:1px;text-transform:uppercase;display:flex;align-items:center;gap:18px}
.eyebrow::after{content:"";width:72px;height:2px;background:var(--sky)}
.eyebrow.light{color:var(--ice)}
.eyebrow.light::after{background:var(--mist)}
.brand{display:flex;align-items:center;gap:10px;font-family:"Inter",sans-serif;font-weight:700;font-size:26px;letter-spacing:2px;text-transform:uppercase}
.brand i{width:14px;height:14px;background:currentColor;display:block}
.topbar{top:0;left:0;width:1200px;height:28px;background:var(--blue-deep);color:#fff;font-size:10px;text-align:center;line-height:28px}
.hero{top:28px;left:0;width:1200px;height:714px;background:linear-gradient(90deg,#002a5c 0%,#003E80 45%,#0054AA 72%,#002a5c 100%)}
.hero-photo{right:170px;top:60px;width:420px;height:654px;background:radial-gradient(ellipse at 50% 45%,#0677BA 0%,#0a4a8f 50%,transparent 75%)}
.nav a{position:absolute;top:66px;color:#fff;font-size:11px;text-decoration:none}
.hero h1{top:208px;left:100px;font-size:70px;line-height:72px;color:#fff}
.hero h1 span{color:var(--sky)}
.dots{right:45px;top:335px;width:14px;height:64px;border:1px solid #fff;border-radius:8px;display:flex;flex-direction:column;align-items:center;justify-content:space-evenly;padding:6px 0}
.dots i{width:4px;height:4px;border-radius:50%;background:#fff}
.welcome{top:742px;left:0;width:1200px;height:823px;background:var(--ice)}
.video{left:100px;top:304px;width:532px;height:394px;border-radius:10px;background:linear-gradient(160deg,#0054AA 0%,#0a3f7e 45%,#0b2547 100%);border:2px solid var(--blue-mid)}
.play{position:absolute;right:50px;bottom:40px;width:42px;height:42px;border-radius:50%;background:rgba(11,37,71,.85);display:flex;align-items:center;justify-content:center}
.stat b{display:block;font-family:"Archivo",sans-serif;font-weight:800;font-size:30px}
.stat small{font-size:10px;color:var(--muted)}
.copy p{font-size:13.5px;line-height:22.5px;color:#33475e;margin-bottom:20px}
.seen{top:1565px;left:0;width:1200px;height:201px;background:#fff}
.press{top:107px;left:-20px;display:flex;white-space:nowrap}
.press span{font-family:"Archivo",sans-serif;font-weight:800;font-size:21px;color:var(--blue);width:165px;text-align:center}
.dark{left:0;width:1200px;background:linear-gradient(180deg,var(--blue),var(--blue-deep));color:#fff;overflow:hidden}
.dark h2{font-size:40px;color:#fff}
.dark h2 span{color:var(--sky)}
.card{position:absolute;width:305px;height:345px;background:rgba(6,119,186,.35);border-radius:6px;padding:30px 35px}
.card .inner{position:absolute;inset:14px;border:1px solid rgba(255,255,255,.2);border-radius:4px}
.pill{display:inline-block;font-size:9px;padding:3px 9px;border-radius:10px;margin-right:5px}
.pill.a{background:var(--mist);color:var(--ink)}
.pill.b{border:1px solid var(--sky);color:var(--ice)}
.card h3{font-family:"Archivo",sans-serif;font-weight:800;font-size:14px;line-height:21px;margin-top:18px;text-transform:uppercase}
.card hr{border:0;height:2px;width:48px;background:var(--sky);margin:30px 0 24px}
.card p{font-size:13px;line-height:20px;color:var(--mist)}
.card .link{position:absolute;bottom:46px;left:35px;font-size:10px;color:var(--ice);letter-spacing:.4px}
.track{height:2px;background:rgba(255,255,255,.25);width:700px;left:100px}
.track i{position:absolute;left:0;top:0;height:2px;width:310px;background:var(--mist)}
.studio{top:2580px;left:0;width:1200px;height:985px;background:var(--ice)}
.light-h2{font-size:40px;line-height:52px;color:var(--ink)}
.light-h2 span{color:var(--blue-mid)}
.ph{position:absolute;border-radius:6px}
.insta{top:3565px;left:0;width:1200px;height:740px;background:#fff}
.tile{position:absolute;top:265px;width:237px;height:295px;border-radius:6px;background:linear-gradient(170deg,#0054AA,#0b3a72 55%,#0b2547)}
.footer{top:4985px;left:0;width:1200px;height:372px;background:var(--ice)}
.fi{display:flex;align-items:center;gap:12px;font-size:11px;line-height:15px;color:var(--ink)}
.fi .ic{width:28px;height:28px;border-radius:50%;background:var(--blue);display:flex;align-items:center;justify-content:center}
.fnav a{position:absolute;top:183px;font-size:12px;color:var(--ink);text-decoration:none}
.soc{position:absolute;top:170px;width:34px;height:34px;border-radius:50%;background:var(--blue)}
</style>
</head>
<body>

<div class="abs topbar">New to Quellin? <b>2 Weeks Unlimited · $89</b></div>

<section class="abs hero">
  <div class="abs hero-photo" role="img" aria-label="Athlete in a deep lunge holding a barbell overhead in a dark studio"></div>
  <div class="abs brand" style="left:100px;top:52px;color:#fff"><i></i>Quellin</div>
  <nav class="nav">
    <a style="left:343px">Schedule</a><a style="left:428px">Pricing</a><a style="left:498px">The Studio</a><a style="left:593px">Instructors</a><a style="left:688px">Contact</a>
  </nav>
  <div class="abs" style="left:776px;top:58px;display:flex;align-items:center;gap:10px;color:#fff;font-size:10px">
    <span style="width:26px;height:26px;border-radius:50%;background:#fff;display:flex;align-items:center;justify-content:center">
      <svg width="12" height="12" viewBox="0 0 24 24"><path d="M6.6 10.8a15 15 0 006.6 6.6l2.2-2.2a1 1 0 011-.25 11.4 11.4 0 003.6.6 1 1 0 011 1V20a1 1 0 01-1 1A17 17 0 013 4a1 1 0 011-1h3.5a1 1 0 011 1c0 1.25.2 2.45.6 3.6a1 1 0 01-.25 1z" fill="#0054AA"/></svg>
    </span>
    <span>CALL <b>+1 555.010.2468</b></span>
  </div>
  <div class="btn btn-soft" style="left:968px;top:28px;width:132px;height:40px">Book a Class</div>
  <div class="abs" style="left:100px;top:186px;color:#fff;font-size:13px">Halden, Texas · West Marlow</div>
  <h1 class="abs display">Elevated<br><span>Strength.</span></h1>
  <p class="abs" style="left:100px;top:380px;width:420px;color:#fff;font-size:13.5px;line-height:21px">A boutique Verra studio built to make you feel at home from the moment you walk in — and unstoppable the moment you walk out.</p>
  <div class="btn btn-mid" style="left:100px;top:470px;width:164px;height:40px">Claim Intro Offer</div>
  <div class="btn btn-soft" style="left:277px;top:470px;width:146px;height:40px">View Schedule</div>
  <div class="abs dots"><i></i><i></i><i></i><i></i></div>
</section>

<section class="abs welcome">
  <div class="abs eyebrow" style="left:100px;top:122px;color:var(--ink)">New Here</div>
  <h2 class="abs display light-h2" style="left:97px;top:152px;font-size:41px;line-height:52px">Welcome to your<br>first <span>class.</span></h2>
  <div class="abs video" role="img" aria-label="Placeholder for studio video: member training on a reformer under blue light">
    <div class="play"><svg width="12" height="14" viewBox="0 0 12 14"><path d="M0 0l12 7-12 7z" fill="#fff"/></svg></div>
  </div>
  <div class="abs" style="left:706px;top:126px;display:flex">
    <div class="stat" style="width:112px;padding-right:20px;border-right:1px solid var(--mist)"><b>45</b><small>Min sessions</small></div>
    <div class="stat" style="width:160px;padding:0 30px;border-right:1px solid var(--mist)"><b>10+</b><small>Classes / week</small></div>
    <div class="stat" style="padding-left:30px"><b>04</b><small>Texas studios</small></div>
  </div>
  <div class="abs copy" style="left:706px;top:238px;width:395px">
    <p>Quellin is a boutique Verra studio with a flagship location in Halden, Texas. The second location recently opened in West Marlow, TX with upcoming expansion plans into Ridgeway, TX (Fall 2026) and Corland, TX (Spring 2027). At Quellin, we believe strength is for everyone. Our mission is to make clients feel comfortable from the moment they walk through our doors while delivering workouts that challenge, empower, and keep them coming back.</p>
    <p>Our brand is elevated without feeling exclusive, polished without feeling cold. Every detail—from the studio to the website—should feel welcoming, intentional, and easy to experience. We want visitors to leave with the same feeling our clients do after class: confident, energized, and already looking</p>
  </div>
  <div class="btn btn-primary" style="left:708px;top:632px;width:138px;height:40px">Learn More</div>
</section>

<section class="abs seen">
  <div class="abs" style="left:0;width:1200px;top:52px;text-align:center;font-size:15px;letter-spacing:1px">AS SEEN IN</div>
  <div class="abs press"><span>DAYBREAK</span><span>LEDGER</span><span>ACTIVE LIFE</span><span>LUSTRE</span><span>FOLIO</span><span>CALM+KIND</span><span>VELOUR</span><span>ROAM+REST</span></div>
</section>

<section class="abs dark" style="top:1766px;height:814px">
  <div class="abs eyebrow light" style="left:103px;top:112px">Our Schedule</div>
  <h2 class="abs display" style="left:100px;top:150px">Book your next <span>class.</span></h2>
  <div class="btn btn-light" style="left:922px;top:158px;width:176px;height:38px">Open Full Schedule</div>
  <div class="card" style="left:100px;top:258px"><div class="inner"></div><span class="pill a">5:30 AM</span><span class="pill b">3 SPOTS</span><h3>Quellin 45<br>with Tessa K.</h3><hr><p>Sed ut perspiciatis unde omnis iste natus error sit voluptatem santium doloremque laudantium</p><div class="link">BOOK A CLASS →</div></div>
  <div class="card" style="left:437px;top:258px"><div class="inner"></div><span class="pill a">6:30 AM</span><span class="pill b">6 SPOTS</span><h3>Quellin 45<br>with Nora P.</h3><hr><p>Sed ut perspiciatis unde omnis iste natus error sit voluptatem santium doloremque laudantium</p><div class="link">BOOK A CLASS →</div></div>
  <div class="card" style="left:774px;top:258px"><div class="inner"></div><span class="pill a">9:00 AM</span><span class="pill b">8 SPOTS</span><h3>Quellin Slow<br>with Jules A.</h3><hr><p>Sed ut perspiciatis unde omnis iste natus error sit voluptatem santium doloremque laudantium</p><div class="link">BOOK A CLASS →</div></div>
  <div class="card" style="left:1111px;top:258px"><div class="inner"></div><span class="pill a">5:30 AM</span><span class="pill b">3 SPOTS</span><h3>Quellin 45<br>with Tessa K.</h3><hr><p>Sed ut perspiciatis unde omnis iste natus error sit voluptatem santium doloremque laudantium</p><div class="link">BOOK A CLASS →</div></div>
  <div class="abs track" style="top:677px"><i></i></div>
</section>

<section class="abs studio">
  <div class="abs eyebrow" style="left:100px;top:95px">The Studio</div>
  <h2 class="abs display light-h2" style="left:97px;top:122px">A space designed<br>to feel <span>like yours.</span></h2>
  <p class="abs" style="left:733px;top:95px;width:370px;font-size:13.5px;line-height:22px;color:#33475e">Warm light, considered finishes, and Arcformers spaced so you can actually breathe. We built Quellin around one idea: a workout studio that doesn't feel like a gym.</p>
  <div class="ph" style="left:100px;top:265px;width:513px;height:550px;background:linear-gradient(170deg,#0677BA,#0054AA 45%,#0b2547 85%)" role="img" aria-label="Member seen from behind gripping reformer straps in a blue-lit studio"></div>
  <div class="ph" style="left:620px;top:265px;width:236px;height:218px;background:linear-gradient(160deg,#7BADD7,#0677BA 55%,#0b2547)" role="img" aria-label="Member performing a reformer exercise on her back"></div>
  <div class="ph" style="left:863px;top:265px;width:237px;height:218px;background:linear-gradient(160deg,#0054AA,#0677BA 55%,#0b2547)" role="img" aria-label="Member in blue activewear kneeling on a reformer"></div>
  <div class="ph" style="left:620px;top:490px;width:480px;height:325px;background:linear-gradient(165deg,#0677BA,#0a3f7e 50%,#0b2547)" role="img" aria-label="Member lying on a reformer during a stretch"></div>
  <div class="btn btn-primary" style="left:440px;top:860px;width:164px;height:40px">Claim Intro Offer</div>
  <div class="btn btn-soft" style="left:615px;top:860px;width:146px;height:40px">View Schedule</div>
</section>

<section class="abs insta">
  <div class="abs" style="left:0;width:1200px;top:110px;text-align:center;font-size:15px;letter-spacing:1px">INSTAGRAM</div>
  <h2 class="abs display" style="left:0;width:1200px;top:138px;text-align:center;font-size:40px;color:var(--ink)">Follow @quellinstudio</h2>
  <div class="abs" style="left:560px;top:205px;width:80px;height:2px;background:var(--sky)"></div>
  <div class="tile" style="left:100px" role="img" aria-label="Instructor portrait post for Virgo season"></div>
  <div class="tile" style="left:355px" role="img" aria-label="Instructor portrait post for Taurus season"></div>
  <div class="tile" style="left:610px" role="img" aria-label="Instructor portrait post for Capricorn season"></div>
  <div class="tile" style="left:865px" role="img" aria-label="Instructor portrait post for Leo season"></div>
  <div class="btn btn-primary" style="left:518px;top:610px;width:164px;height:40px;gap:8px">
    <svg width="12" height="12" viewBox="0 0 12 12"><rect x="1" y="1" width="10" height="10" rx="3" fill="none" stroke="#fff" stroke-width="1.3"/></svg>Open Instagram
  </div>
</section>

<section class="abs dark" style="top:4305px;height:680px">
  <div class="abs eyebrow light" style="left:103px;top:112px">Our Locations</div>
  <h2 class="abs display" style="left:100px;top:150px">Four studios. <span>One method.</span></h2>
  <div class="btn btn-light" style="left:922px;top:158px;width:176px;height:38px">Open Full Schedule</div>
  <div class="card" style="left:100px;top:243px;height:252px"><div class="inner"></div>
    <svg class="abs" style="left:35px;top:38px" width="30" height="30" viewBox="0 0 30 30"><circle cx="15" cy="15" r="14" fill="#CADEEF"/><path d="M15 7a5 5 0 00-5 5c0 4 5 10 5 10s5-6 5-10a5 5 0 00-5-5z" fill="#0054AA"/><circle cx="15" cy="12" r="1.8" fill="#CADEEF"/></svg>
    <div class="abs" style="left:80px;top:40px;font-size:9px;color:var(--mist)">FLAGSHIP</div><div class="abs" style="left:80px;top:53px;font-family:Archivo,sans-serif;font-weight:800;font-size:12px">HALDEN</div>
    <div class="abs" style="left:35px;top:100px;font-size:12px;line-height:18px;color:var(--mist)">2210 Linden Rd, Halden, TX<br>Mon–Fri 5:30a–8p · Sat–Sun 7:30a–12p</div>
    <div class="link" style="bottom:48px">BOOK THIS STUDIO →</div></div>
  <div class="card" style="left:437px;top:243px;height:252px"><div class="inner"></div>
    <svg class="abs" style="left:35px;top:38px" width="30" height="30" viewBox="0 0 30 30"><circle cx="15" cy="15" r="14" fill="#CADEEF"/><path d="M15 7a5 5 0 00-5 5c0 4 5 10 5 10s5-6 5-10a5 5 0 00-5-5z" fill="#0054AA"/><circle cx="15" cy="12" r="1.8" fill="#CADEEF"/></svg>
    <div class="abs" style="left:80px;top:40px;font-size:9px;color:var(--mist)">NOW OPEN</div><div class="abs" style="left:80px;top:53px;font-family:Archivo,sans-serif;font-weight:800;font-size:12px">WEST MARLOW</div>
    <div class="abs" style="left:35px;top:100px;font-size:12px;line-height:18px;color:var(--mist)">418 Oak Ave, West Marlow, TX<br>Mon–Fri 6a–7p · Sat 8a–12p</div>
    <div class="link" style="bottom:48px">BOOK THIS STUDIO →</div></div>
  <div class="card" style="left:774px;top:243px;height:252px"><div class="inner"></div>
    <svg class="abs" style="left:35px;top:38px" width="30" height="30" viewBox="0 0 30 30"><circle cx="15" cy="15" r="14" fill="#CADEEF"/><path d="M15 7a5 5 0 00-5 5c0 4 5 10 5 10s5-6 5-10a5 5 0 00-5-5z" fill="#0054AA"/><circle cx="15" cy="12" r="1.8" fill="#CADEEF"/></svg>
    <div class="abs" style="left:80px;top:40px;font-size:9px;color:var(--mist)">COMING FALL 2026</div><div class="abs" style="left:80px;top:53px;font-family:Archivo,sans-serif;font-weight:800;font-size:12px">RIDGEWAY</div>
    <div class="abs" style="left:35px;top:100px;font-size:12px;line-height:18px;color:var(--mist)">Downtown Ridgeway, TX<br>Details coming soon</div>
    <div class="link" style="bottom:48px">BOOK THIS STUDIO →</div></div>
  <div class="card" style="left:1111px;top:243px;height:252px"><div class="inner"></div>
    <svg class="abs" style="left:35px;top:38px" width="30" height="30" viewBox="0 0 30 30"><circle cx="15" cy="15" r="14" fill="#CADEEF"/><path d="M15 7a5 5 0 00-5 5c0 4 5 10 5 10s5-6 5-10a5 5 0 00-5-5z" fill="#0054AA"/><circle cx="15" cy="12" r="1.8" fill="#CADEEF"/></svg>
    <div class="abs" style="left:80px;top:40px;font-size:9px;color:var(--mist)">FLAGSHIP</div><div class="abs" style="left:80px;top:53px;font-family:Archivo,sans-serif;font-weight:800;font-size:12px">HALDEN</div>
    <div class="abs" style="left:35px;top:100px;font-size:12px;line-height:18px;color:var(--mist)">2210 Linden Rd, Halden, TX<br>Mon–Fri 5:30a–8p · Sat–Sun 7:30a–12p</div>
    <div class="link" style="bottom:48px">BOOK THIS STUDIO →</div></div>
  <div class="abs track" style="top:573px"><i></i></div>
</section>

<footer class="abs footer">
  <div class="abs brand" style="left:100px;top:58px;color:var(--blue);font-size:34px"><i style="width:18px;height:18px"></i>Quellin</div>
  <div class="abs fi" style="left:392px;top:62px"><span class="ic"><svg width="12" height="14" viewBox="0 0 12 14"><path d="M6 0a5 5 0 00-5 5c0 4 5 9 5 9s5-5 5-9a5 5 0 00-5-5z" fill="#fff"/><circle cx="6" cy="5" r="1.8" fill="#0054AA"/></svg></span><span>Halden (Flagship)<br>West Marlow Ridgeway</span></div>
  <div class="abs fi" style="left:670px;top:62px"><span class="ic"><svg width="12" height="12" viewBox="0 0 24 24"><path d="M6.6 10.8a15 15 0 006.6 6.6l2.2-2.2a1 1 0 011-.25 11.4 11.4 0 003.6.6 1 1 0 011 1V20a1 1 0 01-1 1A17 17 0 013 4a1 1 0 011-1h3.5a1 1 0 011 1c0 1.25.2 2.45.6 3.6a1 1 0 01-.25 1z" fill="#fff"/></svg></span><span>Tel:<br>+1 555.010.2468</span></div>
  <div class="abs fi" style="left:895px;top:62px"><span class="ic"><svg width="12" height="10" viewBox="0 0 12 10"><rect x=".5" y=".5" width="11" height="9" rx="1" fill="none" stroke="#fff"/><path d="M.5 1l5.5 4 5.5-4" fill="none" stroke="#fff"/></svg></span><span>Email:<br>hello@quellinstudio.com</span></div>
  <div class="abs" style="left:100px;top:130px;width:1000px;height:1px;background:var(--mist)"></div>
  <nav class="fnav"><a style="left:100px">Schedule</a><a style="left:218px">Pricing</a><a style="left:318px">The Studio</a><a style="left:448px">Instructors</a><a style="left:578px">Contact</a></nav>
  <span class="soc" style="left:888px"></span><span class="soc" style="left:933px"></span><span class="soc" style="left:978px"></span><span class="soc" style="left:1023px"></span><span class="soc" style="left:1068px"></span>
  <div class="abs" style="left:100px;top:226px;width:1000px;height:1px;background:var(--mist)"></div>
  <div class="abs" style="left:0;width:1200px;top:275px;text-align:center;font-size:12px;color:var(--ink)">Copyright © Quellin Verra, LLC 2026. All rights reserved.</div>
</footer>

</body>
</html>
```